Harrowgate Lending Inc. Investor Presentation

We would like a PowerPoint presentation to attract prospective investors. It needs to look extremely professional since we are a financial lending institution, and seeking capital investors. We specialize in Private Lending with Mortgage Backed Securities, both Residential and Commercial properties.

```html
<!DOCTYPE html>
<html lang="en">
<head>
<meta charset="utf-8">
<title>Harrowgate Lending Inc. — Investor Presentation</title>
<link href="https://fonts.googleapis.com/css2?family=Montserrat:wght@500;600;700;800&family=Arimo:wght@400&display=swap" rel="stylesheet">
<style>
:root{
  --navy:#17197a;
  --navy-deep:#121466;
  --gold:#e2b730;
  --gold-soft:#f1dc97;
  --ink:#3a3a3a;
  --page:#f1f1f3;
  --white:#ffffff;
}
*{box-sizing:border-box;margin:0;padding:0}
html,body{width:1200px;height:4208px;overflow:hidden;background:var(--page)}
body{position:relative;font-family:"Arimo",Arial,sans-serif;color:var(--ink)}
.slide{position:absolute;left:51px;width:1097px;height:617px;background:var(--white);overflow:hidden;box-shadow:0 1px 4px rgba(0,0,0,.12)}
.abs{position:absolute}
.photo{position:absolute;inset:0;width:100%;height:100%}
.title{position:absolute;font-family:"Montserrat",sans-serif;font-weight:800;font-size:41px;color:var(--navy);letter-spacing:.5px;line-height:1;padding:0 6px;
  background:linear-gradient(to bottom,transparent 62%,var(--gold) 62%)}
.body-copy{position:absolute;font-size:12.5px;line-height:25.5px;color:var(--ink);text-align:justify}
.body-copy p+p{margin-top:25px}
.brand{position:absolute;font-family:"Montserrat",sans-serif;font-weight:600;color:var(--navy);text-transform:uppercase;display:flex;align-items:center;gap:8px;line-height:1.15}
.brand .mark{width:10px;height:10px;background:var(--gold);flex:none}
.brand.small{font-size:9px;right:20px;top:22px}
/* cover */
.cover-head{left:34px;top:340px;font-family:"Montserrat",sans-serif;font-weight:700;font-size:22px;line-height:39px;color:var(--navy);text-transform:uppercase}
.cover-sub{left:36px;top:431px;font-size:17px;color:#444}
/* services */
.service-title{position:absolute;font-family:"Montserrat",sans-serif;font-weight:600;font-size:17px;color:var(--navy);text-transform:uppercase;white-space:nowrap}
.service-desc{position:absolute;font-size:13px;line-height:24px;color:#444;width:500px}
/* properties */
.prop-card{position:absolute;top:110px;width:326px;height:418px}
.prop-label{position:absolute;left:28px;top:388px;width:271px;height:70px;text-align:center;color:var(--white);padding-top:17px}
.prop-label strong{display:block;font-family:"Montserrat",sans-serif;font-weight:700;font-size:18px;text-transform:uppercase;line-height:1.1}
.prop-label span{font-size:15px}
.gold{background:var(--gold)} .navy{background:var(--navy)}
/* closing */
.closing{background:var(--navy)}
.thanks-frame{position:absolute;left:170px;top:207px;width:759px;height:323px;border:1.5px solid var(--gold)}
.thanks{position:absolute;left:0;right:0;top:42px;text-align:center;font-family:"Montserrat",sans-serif;font-weight:800;font-size:84px;color:var(--white);letter-spacing:1px}
.contact{position:absolute;top:158px;width:220px;margin-left:-110px;text-align:center;color:var(--white);font-size:13.5px;line-height:18px}
.contact .ring{width:68px;height:68px;border:2px solid var(--white);border-radius:50%;margin:0 auto 10px;display:flex;align-items:center;justify-content:center}
</style>
</head>
<body>

<!-- Cover -->
<section class="slide" style="top:70px">
  <div class="photo" role="img" aria-label="Young family sitting on a living room rug under a cardboard roof, holding a potted plant" style="background:linear-gradient(90deg,#fafaf9 0%,#f6f3ef 38%,#cdb79c 60%,#8a6b4d 78%,#b7a38d 100%)"></div>
  <svg class="abs" style="left:0;top:0" width="122" height="106"><polygon points="0,0 122,0 0,106" fill="var(--navy)"/></svg>
  <svg class="abs" style="right:0;bottom:0" width="112" height="100"><polygon points="112,0 112,100 0,100" fill="var(--gold)"/></svg>
  <svg class="abs" style="left:50px;top:486px" width="210" height="140"><circle cx="105" cy="105" r="82" fill="none" stroke="var(--gold)" stroke-width="28" opacity=".12"/></svg>
  <div class="brand" style="left:40px;top:218px;font-size:28px"><span class="mark" style="width:22px;height:22px"></span><span>Harrowgate<br>Lending</span></div>
  <div class="abs cover-head">Sed ut perspiciatis unde omnis<br>iste natus error sit volupe</div>
  <div class="abs cover-sub">Sed ut perspiciatis unde omnis iste natus error sit</div>
</section>

<!-- About -->
<section class="slide" style="top:767px">
  <svg class="abs" style="left:0;top:0" width="540" height="617" role="img" aria-label="Smiling older couple embracing at a kitchen table">
    <polygon points="0,0 243,0 488,311 243,617 0,617" fill="#c9b7a2"/>
    <polygon points="412,200 516,311 412,422 444,422 532,311 444,200" fill="var(--gold)"/>
  </svg>
  <div class="brand small"><span class="mark"></span><span>Harrowgate<br>Lending</span></div>
  <div class="title" style="left:538px;top:96px">ABOUT US</div>
  <div class="body-copy" style="left:534px;top:172px;width:502px">
    <p>Sed ut perspiciatis unde omnis iste natus error sit voluptatem accusantium dolor emque laudantium, totam rem aperiam, eaque ipsa quae ab illo inventore veritatis et quasi architecto beatae vitae dicta sunt explicabo. Nemo enim ipsam voluptatem quia voluptas sit aspernatur aut odit aut fugit, sed quia consequuntur magni dolores eos qui ratione voluptatem sequi nesciunt. Neque porro quisquam est, qui dolorem ipsum quia dolor sit amet, consectetur, adipisci velit, sed quia non numquam eius ut labore et dolore magnam aliquam quaerat voluptatem.</p>
    <p>Nemo enim ipsam voluptatem quia voluptas sit aspernatur aut odit aut fugit, sed quia consequuntur magni dolores eos qui ratione voluptatem sequi nesciunt. Neque porro quisquam est, qui dolorem ipsum quia dolor sit amet, consectetur, adipisci velit, sed quia non numquam eius modi tempora incidunt ut labore et dolore magnam aliquam quaerat voluptatem. Ut enim ad minima veniam, quis nostrum suscipit laboriosam, nisi ut aliquid ex ea commodi consequatur..</p>
  </div>
</section>

<!-- Services -->
<section class="slide" style="top:1455px">
  <svg class="abs" style="left:0;top:0" width="1097" height="617">
    <polygon points="686,0 1097,0 1097,366" fill="#b89a7c" role="img" aria-label="Hands holding a small model house"/>
    <polygon points="0,257 414,617 0,617" fill="#c08a72" role="img" aria-label="Cupped hands holding a paper family cut-out"/>
    <line x1="0" y1="214" x2="262" y2="452" stroke="var(--gold)" stroke-width="1" opacity=".6"/>
    <line x1="832" y1="172" x2="1097" y2="420" stroke="var(--gold)" stroke-width="1" opacity=".6"/>
  </svg>
  <div class="brand small"><span class="mark"></span><span>Harrowgate<br>Lending</span></div>
  <div class="title" style="left:46px;top:40px">SERVICES</div>

  <svg class="abs" style="left:145px;top:134px" width="150" height="110">
    <polygon points="6,106 80,4 144,106" fill="var(--gold)"/><polygon points="0,100 76,0 140,100" fill="var(--navy)"/>
    <g fill="none" stroke="#fff" stroke-width="2"><rect x="58" y="48" width="28" height="36" rx="2"/><line x1="64" y1="60" x2="80" y2="60"/><line x1="64" y1="68" x2="80" y2="68"/><line x1="64" y1="76" x2="74" y2="76"/></g>
  </svg>
  <div class="service-title" style="left:310px;top:146px">Mortgage Backed Securities</div>
  <div class="service-desc" style="left:312px;top:177px">Sed ut perspiciatis unde omnis iste natus error sit voluptatem accusantium doloremque laudantium, totam rem aperiam, eaque ipsa</div>

  <svg class="abs" style="left:264px;top:284px" width="150" height="110">
    <polygon points="6,106 80,4 144,106" fill="var(--navy)"/><polygon points="0,100 76,0 140,100" fill="var(--gold)"/>
    <g fill="none" stroke="#fff" stroke-width="2"><polyline points="56,66 74,50 92,66"/><rect x="61" y="64" width="26" height="22"/><rect x="70" y="74" width="8" height="12"/></g>
  </svg>
  <div class="service-title" style="left:428px;top:298px">Residential Properties</div>
  <div class="service-desc" style="left:430px;top:329px">Sed ut perspiciatis unde omnis iste natus error sit voluptatem accusantium doloremque laudantium, totam rem aperiam, eaque ipsa</div>

  <svg class="abs" style="left:395px;top:444px" width="150" height="110">
    <polygon points="6,106 80,4 144,106" fill="var(--gold)"/><polygon points="0,100 76,0 140,100" fill="var(--navy)"/>
    <g fill="none" stroke="#fff" stroke-width="2"><rect x="58" y="52" width="20" height="36"/><rect x="78" y="64" width="16" height="24"/><line x1="63" y1="60" x2="73" y2="60"/><line x1="63" y1="68" x2="73" y2="68"/><line x1="63" y1="76" x2="73" y2="76"/><line x1="82" y1="72" x2="90" y2="72"/></g>
  </svg>
  <div class="service-title" style="left:563px;top:458px">Commercial Properties</div>
  <div class="service-desc" style="left:565px;top:489px">Sed ut perspiciatis unde omnis iste natus error sit voluptatem accusantium doloremque laudantium, totam rem aperiam, eaque ipsa</div>
</section>

<!-- Properties -->
<section class="slide" style="top:2144px">
  <div class="brand small"><span class="mark"></span><span>Harrowgate<br>Lending</span></div>
  <div class="title" style="left:38px;top:32px">PROPERTIES</div>
  <div class="prop-card" style="left:28px">
    <div class="photo" role="img" aria-label="Family jumping on a lawn in front of a white house" style="height:418px;background:linear-gradient(180deg,#dfe3df,#9aa79a 55%,#5f8a46)"></div>
    <div class="prop-label gold"><strong>Sed ut perspiciatis</strong><span>Nemo enim ipsam</span></div>
  </div>
  <div class="prop-card" style="left:386px">
    <div class="photo" role="img" aria-label="Family under a cardboard roof in a new home" style="height:418px;background:linear-gradient(180deg,#c9b59a,#b9bcc6 50%,#5a6072)"></div>
    <div class="prop-label navy"><strong>Sed ut perspiciatis</strong><span>Nemo enim ipsam</span></div>
  </div>
  <div class="prop-card" style="left:745px">
    <div class="photo" role="img" aria-label="Model houses on a desk with documents and hands" style="height:418px;background:linear-gradient(180deg,#8d95a8,#c8b8a0 50%,#a07650)"></div>
    <div class="prop-label gold"><strong>Sed ut perspiciatis</strong><span>Nemo enim ipsam</span></div>
  </div>
</section>

<!-- What we do -->
<section class="slide" style="top:2834px">
  <svg class="abs" style="left:0;top:0" width="1097" height="617">
    <polygon points="704,0 1097,0 1097,617 457,617" fill="#8a6450" role="img" aria-label="Several hands holding a white paper house"/>
    <line x1="670" y1="6" x2="474" y2="610" stroke="var(--gold)" stroke-width="1" opacity=".7"/>
  </svg>
  <div class="brand small" style="color:var(--white)"><span class="mark"></span><span>Harrowgate<br>Lending</span></div>
  <div class="title" style="left:34px;top:40px">WHAT WE DO</div>
  <div class="body-copy" style="left:47px;top:138px;width:422px">
    <p>Sed ut perspiciatis unde omnis iste natus error sit voluptatem acc usantium dolor emque laudantium, totam rem aperiam, eaque ipsa quae ab illo inventore veritatis et quasi architecto beatae vitae dicta sunt explicabo. Nemo enim ipsam voluptatem quia voluptas sit aspernatur aut odit aut fugit, sed quia consequuntur magni dolores eos qui ratione voluptatem sequi nesciunt. Neque porro quisquam est, qui dolorem ipsum quia dolor sit amet, consectetur, adipisci velit, sed ut labore et dolore magnam aliquam quaerat voluptatem.</p>
    <p>Nemo enim ipsam voluptatem quia voluptas sit aspernatur aut odit aut fugit, sed quia consequuntur magni dolores eos qui ratione voluptatem sequi nesciunt. Neque porro quisquam est, qui dolorem ipsum quia dolor sit amet, consectetur, adipisci velit, sed quia non numquam eius modi tempora incidunt ut labore et dolore magnam aliquam quaerat nisi ut aliquid ex ea commodi consequatur..</p>
  </div>
</section>

<!-- Closing -->
<section class="slide closing" style="top:3519px">
  <div class="photo" role="img" aria-label="Faint family scene under a navy overlay" style="background:radial-gradient(ellipse at 50% 40%,#22268a,var(--navy-deep) 80%)"></div>
  <div class="brand" style="left:0;right:0;top:66px;justify-content:center;font-size:28px;color:var(--white)"><span class="mark" style="width:22px;height:22px"></span><span>Harrowgate<br>Lending</span></div>
  <div class="thanks-frame">
    <div class="thanks">THANK YOU</div>
    <div class="contact" style="left:142px">
      <div class="ring"><svg width="22" height="26" viewBox="0 0 22 26"><path d="M11 25C4 16 2 12 2 9a9 9 0 0 1 18 0c0 3-2 7-9 16z" fill="none" stroke="#fff" stroke-width="2"/><circle cx="11" cy="9" r="3" fill="none" stroke="#fff" stroke-width="2"/></svg></div>
      Lorem Ipsum Dummy Lorem<br>Ipsum dummy
    </div>
    <div class="contact" style="left:387px">
      <div class="ring"><svg width="22" height="22" viewBox="0 0 24 24"><path d="M6 2l4 5-2 3c1 3 3 5 6 6l3-2 5 4-2 4C11 22 2 13 2 4z" fill="#fff"/></svg></div>
      Phone<br>+1 555 010 4400
    </div>
    <div class="contact" style="left:632px">
      <div class="ring"><svg width="24" height="18" viewBox="0 0 24 18"><rect x="1" y="1" width="22" height="16" rx="2" fill="none" stroke="#fff" stroke-width="2"/><polyline points="1,2 12,10 23,2" fill="none" stroke="#fff" stroke-width="2"/></svg></div>
      Email<br>info@harrowgatelending.com
    </div>
  </div>
</section>

</body>
</html>
```